Tidewell Estates Agency Guarantee

We need a flyer to promote a Sydney based property management agency.
We specialise in Property Management on the Northern Beaches of Sydney. A small boutique agency that prides itself on high quality customer service and the lowest fees.
We would like this flyer to promote our listed features in the document provided and focus on our money back guarantee.
The flyer must:
- be designed to match our website www.tidewellestatesagency.com.au
- Contain our logo and contact details
- Use the attached photoshop template for bleed, sizing and fold lines
- final files must include a print ready PDF and fully editable PSD (photoshop) file with included fonts.
Attached are the following files:
Contact details are:
Name: Tom Hadley
Tel: 0498 316 207
email: tom@tidewellestatesagency.com.au
Office: Level 3, 17 Carrow Rd, Merrigal NSW 2109
Web: www.tidewellestatesagency.com.au
Target Market(s)
35-75yo Male and Females that own investment properties on Sydney's Norther Beaches
Industry/Entity Type
Real Estate
Requirements
Must have
- The flyer must:
- - Be double sided and colour
- - be designed to match our website www.tidewellestatesagency.com.au
- - Contain our logo and contact details
- - Use the attached photoshop template for bleed, sizing and fold lines
- - final files must include a print ready PDF and fully editable PSD (photoshop) file with included fonts.
Nice to have
- A Money back guarantee "stamp"

```html
<!DOCTYPE html>
<html lang="en">
<head>
<meta charset="utf-8">
<title>Tidewell Estates Agency – Property Management Flyer</title>
<link rel="stylesheet" href="https://fonts.googleapis.com/css2?family=Montserrat:wght@300;400;500;600;700;800&display=swap">
<style>
  :root {
    --brand-blue: #27a3d3;
    --panel-blue: #25a0cc;
    --deep-teal: #0e6786;
    --paper-grey: #dedede;
    --ink: #3a3a3a;
    --ink-soft: #4a4a4a;
    --panel-text: #e3f4fb;
    --white: #ffffff;
    --stamp-orange: #f26a2a;
    --stamp-light: #f7915a;
  }
  * { box-sizing: border-box; margin: 0; padding: 0; }
  html, body { width: 1200px; height: 946px; overflow: hidden; background: var(--white); }
  .flyer {
    position: relative; width: 1200px; height: 946px; overflow: hidden;
    font-family: "Montserrat", sans-serif; color: var(--ink);
    background: var(--white);
  }
  .abs { position: absolute; }

  /* backgrounds */
  .shade-left { left: 0; top: 0; width: 400px; height: 341px;
    background: linear-gradient(180deg, #e6e6e6 0%, #d9d9d9 100%); }
  .shade-middle { left: 400px; top: 0; width: 406px; height: 257px;
    background: linear-gradient(180deg, #e2e2e2 0%, #d6d6d6 100%); }
  .band-blue { background: var(--panel-blue); box-shadow: 0 3px 6px rgba(0,0,0,.18); }
  .band-portal { left: 0; top: 341px; width: 400px; height: 251px; }
  .band-tenants { left: 403px; top: 257px; width: 401px; height: 397px; }

  .rule { width: 5px; background: var(--brand-blue); }

  /* typography */
  .heading {
    font-weight: 500; font-size: 17px; line-height: 22px; letter-spacing: .4px;
    text-transform: uppercase; color: var(--brand-blue);
  }
  .heading.on-blue { color: var(--white); }
  .copy {
    font-weight: 300; font-size: 12px; line-height: 21.4px;
    text-align: justify; hyphens: auto; color: var(--ink);
  }
  .copy.on-blue { color: var(--panel-text); }

  .bullets { list-style: none; }
  .bullets li { position: relative; padding-left: 25px; margin-bottom: 14px; }
  .bullets li::before {
    content: ""; position: absolute; left: 0; top: 5px; width: 12px; height: 12px;
    background: var(--brand-blue);
  }

  /* cover panel */
  .cover-photo {
    left: 806px; top: 0; width: 394px; height: 736px;
    background: linear-gradient(180deg, #5fb0e0 0%, #bcdcef 18%, #8a8f96 38%, #5d6b5a 58%, #3f6a3c 72%, #9bb0c4 86%, #d9dfe6 100%);
  }
  .wordmark {
    left: 820px; top: 52px; width: 370px; text-align: right;
    font-weight: 700; color: #111; text-transform: uppercase; letter-spacing: -.3px;
  }
  .wordmark .main { display: block; font-size: 30px; line-height: 32px; }
  .wordmark .sub { display: block; font-size: 10px; line-height: 14px; letter-spacing: 1px; }

  .contact-box { left: 813px; top: 736px; width: 387px; height: 148px; background: var(--panel-blue); }
  .contact { left: 855px; top: 742px; color: var(--white); font-weight: 600; font-size: 12.5px; }
  .contact dl { display: grid; grid-template-columns: 64px 1fr; row-gap: 9.6px; }
  .contact dt, .contact dd { line-height: 17.5px; }
  .website { right: 18px; top: 896px; color: var(--white); font-weight: 600; font-size: 15px; }
</style>
</head>
<body>
<div class="flyer">

  <div class="abs shade-left"></div>
  <div class="abs shade-middle"></div>
  <div class="abs band-blue band-portal"></div>
  <div class="abs band-blue band-tenants"></div>

  <!-- bottom sweep bands -->
  <svg class="abs" style="left:0;top:860px" width="1200" height="86" viewBox="0 860 1200 86">
    <path d="M0,884 Q380,900 735,946 L0,946 Z" fill="var(--deep-teal)"/>
    <path d="M724,946 L813,884 L1200,884 L1200,946 Z" fill="var(--deep-teal)"/>
  </svg>

  <div class="abs rule" style="left:16px;top:156px;height:185px"></div>
  <div class="abs rule" style="left:16px;top:592px;height:142px"></div>
  <div class="abs rule" style="left:401px;top:80px;height:177px"></div>
  <div class="abs rule" style="left:401px;top:654px;height:212px"></div>

  <!-- panel one -->
  <section class="abs" style="left:41px;top:21px;width:318px">
    <h2 class="heading">6 Monthly Property<br>Reports:</h2>
    <p class="copy" style="margin-top:14px">We go above and beyond when it comes to reports on your property’s performance.<br>In conjunction with routine inspections every 6 months, we also produce property valuation reports and in-depth Comparative Market Analysis for your property. These reports detail similar properties within close proximity to yours, how they have performed on the market in both sales and rentals. Included in the report are details on the local market in general and how your property has performed, compares and is currently valued at.</p>
  </section>

  <section class="abs" style="left:41px;top:362px;width:318px">
    <h2 class="heading on-blue">Landlord Portal:</h2>
    <p class="copy on-blue" style="margin-top:10px">At Tidewell Estates we have heavily invested into our cloud-based property management software. With our Landlord Portal, you can log in to download financial reports, live job or maintenance updates as well as detailed photos and videos of your latest inspection. It allows you to stay up-to-date with your property and make sure everything is running the way it should be.</p>
  </section>

  <section class="abs" style="left:41px;top:624px;width:318px">
    <h2 class="heading">Maintenance/<br>Renovation Plan:</h2>
    <p class="copy" style="margin-top:9px">Another service we offer is maintenance and renovation plans.<br>A common misconception with an investment property is that you want to spend as little as possible on the property, to maximize the yield. While our job is to ensure the best financial performance of your property there are two very strong reasons to put together a maintenance/renovation plan for your property.</p>
  </section>

  <!-- panel two -->
  <ul class="abs bullets copy" style="left:447px;top:24px;width:304px;color:var(--ink-soft)">
    <li>Building Equity: Renovations add value to your property, and it might be worth spending $20k on a renovation to increase your properties value up to $60k or more – potentially giving you the equity needed to invest in your next property.</li>
    <li>Ensuring that you aren’t ignoring small maintenance issues that could become expensive big problems in the future.</li>
  </ul>

  <section class="abs" style="left:441px;top:279px;width:314px">
    <h2 class="heading on-blue">Retaining Great Tenants:</h2>
    <p class="copy on-blue" style="margin-top:20px">Here at Tidewell Estates Agency we understand the value of quality tenants. They ensure your investment property is well looked after, rent is paid on time and make our jobs here much easier.<br>We like to let quality tenants know that we appreciate them. From time to time we send out small rewards and gifts to thank them for being great, paying on time and looking after your property.<br>Right now we are sending out a little Christmas gift and card to all our tenants. This is not something we charge landlords for, we just want to hold on to quality tenants and show them our appreciation.</p>
  </section>

  <section class="abs" style="left:439px;top:672px;width:316px">
    <h2 class="heading">Our Broad Team:</h2>
    <p class="copy" style="margin-top:11px">Not only do we have a friendly, professional and efficient property management team – we also work closely with associated builders, accountants and mortgage brokers. So you have access to experienced professionals in all facets of property investment.<br>We work for you and its in our best interest that you get the best advice and service possible to get the most out of your investment.</p>
  </section>

  <!-- cover panel -->
  <div class="abs cover-photo" role="img" aria-label="Photo of modern terraced townhouses with landscaped gardens under a blue sky, with the smiling property manager standing arms folded in the foreground"></div>

  <div class="abs wordmark"><span class="main">Tidewell Estates</span><span class="sub">Agency</span></div>

  <svg class="abs" style="left:1072px;top:425px" width="120" height="190" viewBox="0 0 120 190" role="img" aria-label="Money back guarantee stamp">
    <path d="M38,90 L38,185 L60,165 L82,185 L82,90 Z" fill="var(--stamp-orange)"/>
    <circle cx="60" cy="65" r="60" fill="var(--stamp-orange)"/>
    <circle cx="60" cy="65" r="48" fill="none" stroke="var(--stamp-light)" stroke-width="1.5"/>
    <text x="60" y="62" text-anchor="middle" font-family="Montserrat, sans-serif" font-weight="800" font-style="italic" font-size="10" fill="#fff">MONEY BACK</text>
    <text x="60" y="76" text-anchor="middle" font-family="Montserrat, sans-serif" font-weight="800" font-style="italic" font-size="10" fill="#fff">GUARANTEE</text>
  </svg>

  <div class="abs contact-box"></div>
  <div class="abs contact">
    <dl>
      <dt>Name</dt><dd>: Tom Hadley</dd>
      <dt>Tel</dt><dd>: 0498 316 207</dd>
      <dt>email</dt><dd>: tom@tidewellestatesagency.com.au</dd>
      <dt>Office</dt><dd>: Level 3, 17 Carrow Rd,<br>&nbsp;&nbsp;Merrigal NSW 2109</dd>
    </dl>
  </div>
  <div class="abs website">www.tidewellestatesagency.com.au</div>

</div>
</body>
</html>
```